Business card, invoice design and email signature for accounting firm
Ledgerleaf.Ca
Business card, invoice design and email signature for accounting firm - Financial Services
Creative Brief
Simple
Nora Ashby, BA, CGA
Certified General Accountant
12 Brambly Court Dorchester, ON N0L3K7
nora@ledgerleaf.ca
www.ledgerleaf.ca
we don't need the letterhead and envelope.

```html
<!DOCTYPE html>
<html lang="en">
<head>
<meta charset="utf-8">
<title>Ledgerleaf.Ca – Stationery Set</title>
<link href="https://fonts.googleapis.com/css2?family=Open+Sans:wght@400;600;700&display=swap" rel="stylesheet">
<style>
  :root{
    --purple:#5b2d86;
    --green:#8dc63f;
    --lavender:#e6ddf0;
    --lavender-light:#f3eef8;
    --ink:#4a4a4a;
    --rule:#aaaaaa;
    --paper:#ffffff;
    --backdrop:#ecebe8;
  }
  *{box-sizing:border-box;margin:0;padding:0}
  html,body{width:1200px;height:403px;overflow:hidden}
  body{background:var(--backdrop);font-family:"Open Sans",Arial,sans-serif;color:var(--ink);position:relative}
  .piece{position:absolute;background:var(--paper);box-shadow:0 2px 6px rgba(0,0,0,.18);overflow:hidden}
  .swoosh{position:absolute;left:0;width:100%;display:block}
  .logo{display:flex;align-items:center;gap:4px;font-weight:700;color:var(--purple);white-space:nowrap}
  .logo-dot{border-radius:50%;background:var(--green);flex:none}

  /* business cards */
  .card{width:146px;height:122px}
  .card-front .logo{position:absolute;left:10px;top:12px;font-size:12px}
  .card-front .logo-dot{width:8px;height:8px}
  .card-contact{position:absolute;left:12px;top:38px;font-size:5.4px;line-height:8px;white-space:nowrap}
  .card-contact .name{font-weight:700;color:var(--purple);font-size:6.2px}
  .card-front .swoosh{bottom:0;height:36px}
  .card-back{display:flex;flex-direction:column;align-items:center;justify-content:center;gap:8px}
  .card-back .logo{font-size:13px;color:var(--paper)}
  .card-back .logo-dot{width:9px;height:9px}
  .card-back-green{background:var(--green)}
  .card-back-green .logo-dot{background:var(--purple)}
  .card-back-purple{background:var(--purple)}
  .card-back-line{font-size:5.6px;color:var(--paper);letter-spacing:.3px;white-space:nowrap}

  /* invoices */
  .invoice{width:202px;height:302px;top:84px}
  .invoice .logo{position:absolute;left:12px;top:14px;font-size:11px}
  .invoice .logo-dot{width:8px;height:8px}
  .invoice-fields{position:absolute;left:12px;right:12px;top:40px;font-size:5px}
  .field{display:flex;align-items:flex-end;gap:4px;height:9px}
  .field span{flex:none}
  .field i{flex:1;border-bottom:.6px solid var(--rule)}
  .field-pair{display:flex;gap:14px}
  .field-pair .field{flex:1}
  .line-table{position:absolute;left:12px;right:12px;top:82px;border:.6px solid var(--purple)}
  .line-head{display:grid;grid-template-columns:3fr 1fr 1fr 1fr;background:var(--purple);color:var(--paper);font-size:5px;font-weight:600;height:10px;align-items:center;padding:0 3px}
  .line-row{height:9px;border-top:.5px solid var(--lavender)}
  .line-row:nth-child(even){background:var(--lavender)}
  .line-row:nth-child(odd){background:var(--lavender-light)}
  .totals{position:absolute;right:12px;top:214px;width:70px;font-size:5px}
  .pay-methods{position:absolute;left:12px;right:12px;top:240px;display:flex;justify-content:space-between;font-size:5px}
  .pay-methods label{display:flex;align-items:center;gap:2px}
  .pay-methods b{width:5px;height:5px;border:.6px solid var(--purple);display:inline-block}
  .invoice .swoosh{bottom:0;height:40px}
  .invoice-top-band{position:absolute;top:0;right:0;width:90px;height:8px;background:var(--purple)}

  /* email signatures */
  .signature{width:236px;left:872px}
  .signature .logo{position:absolute;left:12px;font-size:12px}
  .signature .logo-dot{width:8px;height:8px}
  .sig-divider{position:absolute;left:118px;width:.8px;background:var(--green)}
  .sig-text{position:absolute;left:125px;font-size:5.2px;line-height:7.6px;white-space:nowrap}
  .sig-text .name{font-weight:700;color:var(--purple);font-size:6.2px}
  .signature .swoosh{bottom:0;height:20px}
</style>
</head>
<body>

<!-- business cards -->
<section class="piece card card-front" style="left:88px;top:138px">
  <div class="logo"><span class="logo-dot"></span>Ledgerleaf.Ca</div>
  <div class="card-contact">
    <div class="name">Nora Ashby, BA, CGA</div>
    <div>Certified General Accountant</div>
    <div>12 Brambly Court Dorchester, ON N0L3K7</div>
    <div>nora@ledgerleaf.ca</div>
    <div>www.ledgerleaf.ca</div>
  </div>
  <svg class="swoosh" viewBox="0 0 146 36" preserveAspectRatio="none" aria-hidden="true">
    <path d="M0 20 C48 8 96 28 146 6 L146 11 C96 33 48 14 0 25Z" fill="var(--green)"/>
    <path d="M0 28 C48 16 96 34 146 13 L146 36 L0 36Z" fill="var(--purple)"/>
  </svg>
</section>

<section class="piece card card-front" style="left:248px;top:138px">
  <div class="logo"><span class="logo-dot"></span>Ledgerleaf.Ca</div>
  <div class="card-contact">
    <div class="name">Nora Ashby, BA, CGA</div>
    <div>Certified General Accountant</div>
    <div>12 Brambly Court Dorchester, ON N0L3K7</div>
    <div>nora@ledgerleaf.ca</div>
    <div>www.ledgerleaf.ca</div>
  </div>
  <svg class="swoosh" viewBox="0 0 146 36" preserveAspectRatio="none" aria-hidden="true">
    <path d="M0 20 C48 8 96 28 146 6 L146 11 C96 33 48 14 0 25Z" fill="var(--purple)"/>
    <path d="M0 28 C48 16 96 34 146 13 L146 36 L0 36Z" fill="var(--green)"/>
  </svg>
</section>

<section class="piece card card-back card-back-green" style="left:88px;top:272px">
  <div class="logo"><span class="logo-dot"></span>Ledgerleaf.Ca</div>
  <div class="card-back-line">www.ledgerleaf.ca</div>
</section>

<section class="piece card card-back card-back-purple" style="left:248px;top:272px">
  <div class="logo"><span class="logo-dot"></span>Ledgerleaf.Ca</div>
  <div class="card-back-line">Accounting · Bookkeeping · Tax Returns</div>
</section>

<!-- invoice, version one -->
<section class="piece invoice" style="left:427px">
  <div class="logo"><span class="logo-dot"></span>Ledgerleaf.Ca</div>
  <div class="invoice-fields">
    <div class="field-pair">
      <div class="field"><span>Bill To</span><i></i></div>
      <div class="field"><span>Date</span><i></i></div>
    </div>
    <div class="field"><i></i></div>
    <div class="field-pair">
      <div class="field"><i></i></div>
      <div class="field"><span>Invoice No.</span><i></i></div>
    </div>
  </div>
  <div class="line-table">
    <div class="line-head"><span>Description</span><span>Qty</span><span>Rate</span><span>Amount</span></div>
    <div class="line-row"></div><div class="line-row"></div><div class="line-row"></div>
    <div class="line-row"></div><div class="line-row"></div><div class="line-row"></div>
    <div class="line-row"></div><div class="line-row"></div><div class="line-row"></div>
    <div class="line-row"></div><div class="line-row"></div><div class="line-row"></div>
  </div>
  <div class="totals">
    <div class="field"><span>Subtotal</span><i></i></div>
    <div class="field"><span>Total</span><i></i></div>
  </div>
  <div class="pay-methods">
    <label><b></b>Cash</label><label><b></b>Cheque</label><label><b></b>Card</label><label><b></b>Transfer</label>
  </div>
  <svg class="swoosh" viewBox="0 0 202 40" preserveAspectRatio="none" aria-hidden="true">
    <path d="M0 22 C70 6 130 30 202 8 L202 14 C130 36 70 14 0 28Z" fill="var(--green)"/>
    <path d="M0 30 C70 18 130 38 202 16 L202 40 L0 40Z" fill="var(--purple)"/>
  </svg>
</section>

<!-- invoice, version two -->
<section class="piece invoice" style="left:648px">
  <div class="invoice-top-band"></div>
  <div class="logo"><span class="logo-dot"></span>Ledgerleaf.Ca</div>
  <div class="invoice-fields">
    <div class="field-pair">
      <div class="field"><span>Bill To</span><i></i></div>
      <div class="field"><span>Date</span><i></i></div>
    </div>
    <div class="field"><i></i></div>
    <div class="field-pair">
      <div class="field"><i></i></div>
      <div class="field"><span>Invoice No.</span><i></i></div>
    </div>
  </div>
  <div class="line-table">
    <div class="line-head"><span>Description</span><span>Qty</span><span>Rate</span><span>Amount</span></div>
    <div class="line-row"></div><div class="line-row"></div><div class="line-row"></div>
    <div class="line-row"></div><div class="line-row"></div><div class="line-row"></div>
    <div class="line-row"></div><div class="line-row"></div><div class="line-row"></div>
    <div class="line-row"></div><div class="line-row"></div><div class="line-row"></div>
  </div>
  <div class="totals">
    <div class="field"><span>Subtotal</span><i></i></div>
    <div class="field"><span>Total</span><i></i></div>
  </div>
  <div class="pay-methods">
    <label><b></b>Cash</label><label><b></b>Cheque</label><label><b></b>Card</label><label><b></b>Transfer</label>
  </div>
  <svg class="swoosh" viewBox="0 0 202 40" preserveAspectRatio="none" aria-hidden="true">
    <path d="M0 32 L202 32 L202 40 L0 40Z" fill="var(--purple)"/>
  </svg>
</section>

<!-- email signatures -->
<section class="piece signature" style="top:110px;height:84px">
  <div class="logo" style="top:24px"><span class="logo-dot"></span>Ledgerleaf.Ca</div>
  <div class="sig-divider" style="top:12px;height:46px"></div>
  <div class="sig-text" style="top:12px">
    <div class="name">Nora Ashby, BA, CGA</div>
    <div>Certified General Accountant</div>
    <div>12 Brambly Court Dorchester, ON N0L3K7</div>
    <div>nora@ledgerleaf.ca</div>
    <div>www.ledgerleaf.ca</div>
  </div>
  <svg class="swoosh" viewBox="0 0 236 20" preserveAspectRatio="none" aria-hidden="true">
    <path d="M0 11 C80 2 160 16 236 4 L236 8 C160 20 80 6 0 15Z" fill="var(--green)"/>
    <path d="M0 16 C80 8 160 20 236 9 L236 20 L0 20Z" fill="var(--purple)"/>
  </svg>
</section>

<section class="piece signature" style="top:222px;height:58px">
  <div class="logo" style="top:20px"><span class="logo-dot"></span>Ledgerleaf.Ca</div>
  <div class="sig-divider" style="top:9px;height:40px"></div>
  <div class="sig-text" style="top:10px">
    <div class="name">Nora Ashby, BA, CGA</div>
    <div>Certified General Accountant</div>
    <div>nora@ledgerleaf.ca</div>
    <div>www.ledgerleaf.ca</div>
  </div>
</section>

<section class="piece signature" style="top:292px;height:72px">
  <div class="logo" style="top:20px"><span class="logo-dot"></span>Ledgerleaf.Ca</div>
  <div class="sig-divider" style="top:9px;height:40px"></div>
  <div class="sig-text" style="top:10px">
    <div class="name">Nora Ashby, BA, CGA</div>
    <div>Certified General Accountant</div>
    <div>12 Brambly Court Dorchester, ON N0L3K7</div>
    <div>www.ledgerleaf.ca</div>
  </div>
  <svg class="swoosh" viewBox="0 0 236 20" preserveAspectRatio="none" aria-hidden="true">
    <path d="M0 12 C80 3 160 18 236 5 L236 20 L0 20Z" fill="var(--purple)"/>
  </svg>
</section>

</body>
</html>
```